Bussines Card - TR EDIFICACIONES, S.A.

We need a design for a business card.
I want it to look professional, but not old fashion.
We are like "young people', somehow i want it to look fresh, new, different, but still serious and professional.
I could use, a non typical design. (I mean, not just rectangular design).

The company Name is " TR EDIFICACIONES, S.A. " we are Panamenian company (spanish language) dedicated to construction and civil engeniering.

The company logo is attached, i use it with white background. Im not sure trying different one, could try.

Industry/Entity Type

Business

```html
<!DOCTYPE html>
<html lang="es">
<head>
<meta charset="utf-8">
<title>TR Edificaciones — Tarjeta de presentación</title>
<link rel="stylesheet" href="https://fonts.googleapis.com/css2?family=Open+Sans:wght@400;600;700&display=swap">
<style>
  :root {
    --stage: #e4e4e4;
    --ink-black: #0b0b0b;
    --ink-dark: #3a3a3a;
    --ink-mid: #5a5a5a;
    --paper: #f7f7f5;
    --accent-red: #e3213b;
    --white: #ffffff;
  }
  * { box-sizing: border-box; margin: 0; padding: 0; }
  html, body {
    width: 1200px; height: 999px; overflow: hidden;
    background: var(--stage);
    font-family: "Open Sans", Arial, sans-serif;
  }
  .stage {
    position: relative; width: 1200px; height: 999px;
  }
  .card {
    position: absolute; left: 190px; width: 820px; height: 450px;
    box-shadow: 0 6px 18px rgba(0,0,0,0.18);
    overflow: hidden;
  }
  .card--front { top: 36px; background: linear-gradient(160deg, #1b1b1b 0%, var(--ink-black) 55%, #151515 100%); }
  .card--back { top: 513px; background: var(--paper); }

  /* Front */
  .front-brand {
    position: absolute; left: 0; right: 0; top: 128px;
    display: flex; flex-direction: column; align-items: center;
  }
  .brand-square {
    display: block; width: 118px; height: 118px; background: var(--white);
  }
  .brand-name {
    margin-top: 26px; color: var(--white);
    font-weight: 700; font-size: 22px; letter-spacing: 3.5px;
  }

  /* Back */
  .accent-bar { position: absolute; width: 14px; background: var(--accent-red); }
  .accent-bar--left { left: 0; top: 110px; height: 70px; }
  .accent-bar--right { right: 0; top: 270px; height: 90px; }

  .back-brand {
    position: absolute; left: 120px; top: 120px;
    display: flex; flex-direction: column; align-items: center;
  }
  .brand-square--dark { width: 112px; height: 112px; background: var(--ink-dark); }
  .brand-name--dark {
    margin-top: 22px; color: var(--ink-dark);
    font-size: 18px; letter-spacing: 2.6px;
  }

  .person { position: absolute; left: 440px; top: 128px; }
  .person-name { color: var(--accent-red); font-weight: 700; font-size: 25px; }
  .person-role { color: var(--ink-mid); font-size: 17px; margin-top: -2px; }

  .contact-list { list-style: none; margin-top: 34px; }
  .contact-item {
    display: flex; align-items: flex-start; gap: 16px;
    color: var(--ink-dark); font-size: 17px; line-height: 1.3;
    margin-bottom: 12px;
  }
  .contact-icon { flex: none; width: 22px; height: 22px; margin-top: 1px; }
</style>
</head>
<body>
<main class="stage">

  <section class="card card--front" aria-label="Cara frontal">
    <div class="front-brand">
      <span class="brand-square" aria-hidden="true"></span>
      <span class="brand-name">TR EDIFICACIONES</span>
    </div>
  </section>

  <section class="card card--back" aria-label="Cara posterior">
    <span class="accent-bar accent-bar--left"></span>
    <span class="accent-bar accent-bar--right"></span>

    <div class="back-brand">
      <span class="brand-square brand-square--dark" aria-hidden="true"></span>
      <span class="brand-name brand-name--dark">TR EDIFICACIONES</span>
    </div>

    <div class="person">
      <p class="person-name">PERSON NAME</p>
      <p class="person-role">Designation</p>

      <ul class="contact-list">
        <li class="contact-item">
          <svg class="contact-icon" viewBox="0 0 22 22" aria-hidden="true">
            <rect width="22" height="22" rx="3" fill="#3a3a3a"/>
            <path d="M5 11 L11 5.5 L17 11 H15 V16.5 H12.3 V13 H9.7 V16.5 H7 V11 Z" fill="#fff"/>
          </svg>
          <span>Calle 48, Bella Vista<br>Torre Alameda, 2do Piso Local 4</span>
        </li>
        <li class="contact-item">
          <svg class="contact-icon" viewBox="0 0 22 22" aria-hidden="true">
            <rect width="22" height="22" rx="3" fill="#3a3a3a"/>
            <path d="M7 5 L9.5 5 L10.5 8.5 L9 9.8 C9.8 11.6 10.6 12.5 12.2 13.2 L13.5 11.7 L17 12.7 L17 15 C17 16 16 17 15 17 C9.5 16.6 5.4 12.5 5 7 C5 6 6 5 7 5 Z" fill="#fff"/>
          </svg>
          <span>265-4710 (O)<br>000 333 4444 (M)</span>
        </li>
        <li class="contact-item">
          <svg class="contact-icon" viewBox="0 0 22 22" aria-hidden="true">
            <rect width="22" height="22" rx="3" fill="#3a3a3a"/>
            <rect x="5" y="7" width="12" height="8.5" fill="none" stroke="#fff" stroke-width="1.5"/>
            <path d="M5 7 L11 12 L17 7" fill="none" stroke="#fff" stroke-width="1.5"/>
          </svg>
          <span>contacto@tredificaciones.com</span>
        </li>
      </ul>
    </div>
  </section>

</main>
</body>
</html>
```